Local 7K Joint Optical Promotion Flyer

A flyer to give to a customer group promoting two optical New York City offices and enticing members to come in and use their optical benefits. Flyer should promote use of benefits at our offices and bring covered patients in for exams and eyewear. We will offer $25 off in addition to covered benefits on the flyer.

Target Market(s)

Eye exam and eyeglass customers with covered benefits usable at our offices.

Industry/Entity Type

Group

Requirements
Must have
• Our businesses address and contact info, expiration date of March 31, 2017, ability to update the expiration date on my own, ability to change the group name on my own. Also must be able to have a black and white version along with the color version. Our two logos are attached, as well as a blank logo. Also, the previous flyer we were using is attached as the pmrv2d file.
Nice to have
• Visual enticement to come in to our offices and use their coverage

```html
<!DOCTYPE html>
<html lang="en">
<head>
<meta charset="utf-8">
<title>PMRV Local 7K – 2017 Eye Glasses Benefit</title>
<link rel="stylesheet" href="https://fonts.googleapis.com/css2?family=Barlow:wght@400;500;600;800&display=swap">
<style>
  :root{
    --ink:#3f5670;
    --ink-soft:#4f6379;
    --side:#dfe7f3;
    --band:#a9c1dc;
    --rule:#3b8fd6;
    --mark:#c9d6e8;
    --white:#ffffff;
    --dark:#1d2a36;
  }
  *{margin:0;padding:0;box-sizing:border-box}
  html,body{width:927px;height:1200px;overflow:hidden;background:var(--white)}
  body{font-family:"Barlow",sans-serif;color:var(--ink);position:relative}
  .flyer{position:relative;width:927px;height:1200px;overflow:hidden;background:var(--white)}
  .side-panel{position:absolute;left:562px;top:0;width:365px;height:1200px;background:var(--side)}
  .offer-band{position:absolute;left:0;top:934px;width:562px;height:266px;background:var(--band)}
  .hero{position:absolute;left:0;top:0;width:927px;height:500px}
  .hero-title{position:absolute;left:54px;top:70px;color:var(--white);font-weight:500;font-size:63px;line-height:66px;letter-spacing:-0.5px}
  .hero-sub{position:absolute;left:54px;top:278px;color:var(--white);font-weight:500;font-size:23px;line-height:34px}
  .entitled{position:absolute;left:54px;top:518px}
  .entitled h2{font-weight:600;font-size:29px;line-height:42px;color:var(--ink)}
  .benefits{list-style:none;margin-top:20px;width:400px}
  .benefits li{position:relative;padding-left:20px;font-size:17.6px;line-height:25px;color:var(--ink-soft);margin-bottom:15px}
  .benefits li::before{content:"•";position:absolute;left:0;top:0}
  .call{font-size:21px;line-height:30px;color:var(--ink-soft);margin-top:8px}
  .call strong{font-weight:600;color:var(--ink)}
  .offer-title{position:absolute;left:54px;top:962px;font-weight:500;font-size:23px;color:var(--ink)}
  .offer-text{position:absolute;left:54px;top:1004px;width:440px;font-size:18px;line-height:26px;color:var(--ink-soft)}
  .offer-text strong{font-weight:600;color:var(--ink)}
  .cut-line{position:absolute;left:0;top:1070px}
  .coupon-amount{position:absolute;left:52px;top:1096px;font-weight:800;font-size:70px;line-height:72px;color:var(--ink);letter-spacing:-2px;white-space:nowrap}
  .coupon-amount sup{font-size:28px;vertical-align:top;position:relative;top:6px;margin-right:2px}
  .coupon-divider{position:absolute;left:268px;top:1112px;width:1px;height:50px;background:var(--ink)}
  .coupon-terms{position:absolute;left:290px;top:1109px;width:238px;font-size:13px;line-height:19px;color:var(--ink-soft)}
  .locations-intro{position:absolute;left:617px;top:522px;font-size:16px;line-height:23px;color:var(--ink-soft)}
  .office{position:absolute;left:617px;width:300px}
  .office-mark{width:46px;height:46px;border-radius:50%;background:var(--mark);margin:0 0 2px 80px}
  .office-name{width:210px;border-top:3px solid var(--rule);border-bottom:3px solid var(--rule);padding:5px 0 4px;font-size:21.5px;line-height:26px;font-weight:500;color:var(--dark);white-space:nowrap}
  .contact{list-style:none;margin-top:12px}
  .contact li{display:flex;align-items:flex-start;gap:12px;font-size:16.5px;line-height:23px;color:var(--dark);margin-bottom:3px}
  .contact svg{flex:none;margin-top:4px}
  .hours{margin-top:8px;font-size:13px;line-height:19px;color:var(--dark)}
  .hours .row{display:flex}
  .hours .days{width:92px}
  .hours strong{font-weight:600}
</style>
</head>
<body>
<main class="flyer">
  <div class="side-panel"></div>
  <div class="offer-band"></div>

  <svg class="hero" viewBox="0 0 927 500" width="927" height="500" role="img" aria-label="Photo of a smiling woman adjusting her new eyeglasses">
    <defs>
      <linearGradient id="heroTone" x1="0" y1="0" x2="1" y2="0.4">
        <stop offset="0" stop-color="#1f2c3a"/>
        <stop offset="0.35" stop-color="#6b6a68"/>
        <stop offset="0.6" stop-color="#d8b89a"/>
        <stop offset="0.85" stop-color="#c9a978"/>
        <stop offset="1" stop-color="#e6e2da"/>
      </linearGradient>
    </defs>
    <path d="M0 0 H927 V256 C860 380 760 470 656 488 C620 440 600 380 588 360 C560 400 530 416 512 416 C480 410 450 380 436 352 C410 390 385 416 360 416 C330 410 300 380 284 368 C260 440 220 480 184 480 C100 470 30 390 0 296 Z" fill="url(#heroTone)"/>
    <path d="M927 256 C860 380 760 470 656 488 C620 440 600 380 588 360 C560 400 530 416 512 416 C480 410 450 380 436 352 C410 390 385 416 360 416 C330 410 300 380 284 368 C260 440 220 480 184 480" fill="none" stroke="#ffffff" stroke-width="2"/>
    <path d="M927 300 C880 420 800 490 720 500" fill="none" stroke="#ffffff" stroke-opacity="0.6" stroke-width="1.5"/>
  </svg>

  <h1 class="hero-title">PMRV Local<br>7K Members &amp;<br>Dependents</h1>
  <p class="hero-sub">Your 2017 Eye Glasses<br>Benefit</p>

  <section class="entitled">
    <h2>What you are entitled to at<br>Hale and Brook Eyecare and<br>Dover Optical at NO COST to you:</h2>
    <ul class="benefits">
      <li>A thorough and professional eye examination checking both eye health and vision</li>
      <li>A Wide Selection of frames fully covered by your plan</li>
      <li>Standard eye glass lenses customized to your prescription</li>
    </ul>
    <p class="call">Call <strong>212-555-0148</strong> or <strong>212-555-0172</strong><br>for an appointment</p>
  </section>

  <h3 class="offer-title">A Special Offer Just For You!</h3>
  <p class="offer-text">This coupon entitles you to <strong>$25 Off</strong> any purchase beyond covered allowance.</p>

  <svg class="cut-line" width="580" height="20" viewBox="0 0 580 20" aria-hidden="true">
    <line x1="0" y1="10" x2="545" y2="10" stroke="#3f5670" stroke-width="1.6" stroke-dasharray="7 6"/>
    <g fill="none" stroke="#1d2a36" stroke-width="1.6">
      <line x1="540" y1="4" x2="566" y2="14"/>
      <line x1="540" y1="16" x2="566" y2="6"/>
      <circle cx="569" cy="5" r="3.5"/>
      <circle cx="569" cy="15" r="3.5"/>
    </g>
  </svg>

  <div class="coupon-amount"><sup>$</sup>25 off</div>
  <div class="coupon-divider"></div>
  <p class="coupon-terms">Upon the use of your optical benefits at your next visit at either of our 2 locations. Expires 03/31/17.</p>

  <p class="locations-intro">Your Optical Benefits are<br>available at:</p>

  <section class="office" style="top:585px">
    <div class="office-mark"></div>
    <div class="office-name">Dover Optical Group</div>
    <ul class="contact">
      <li>
        <svg width="15" height="14" viewBox="0 0 15 14"><path d="M7.5 1 L14 7 H12 V13 H9 V9 H6 V13 H3 V7 H1 Z" fill="#3b8fd6"/></svg>
        <span>118 Carver Avenue, 2nd Floor<br>Between 14th &amp; 15th Streets</span>
      </li>
      <li>
        <svg width="15" height="15" viewBox="0 0 15 15"><circle cx="7.5" cy="7.5" r="6.5" fill="none" stroke="#3b8fd6" stroke-width="1.3"/><path d="M5 4 L6.5 4 L7 6 L6 6.8 C6.5 8 7.2 8.7 8.2 9.2 L9 8.2 L11 8.7 L11 10.2 C8 10.6 4.6 7.2 5 4 Z" fill="#3b8fd6"/></svg>
        <span>(212) 555-0148</span>
      </li>
      <li>
        <svg width="15" height="15" viewBox="0 0 15 15" fill="none" stroke="#3b8fd6" stroke-width="1.2"><circle cx="7.5" cy="7.5" r="6.5"/><ellipse cx="7.5" cy="7.5" rx="3" ry="6.5"/><line x1="1" y1="7.5" x2="14" y2="7.5"/><line x1="2" y1="4.3" x2="13" y2="4.3"/><line x1="2" y1="10.7" x2="13" y2="10.7"/></svg>
        <span>www.doveropticalgroup.com</span>
      </li>
    </ul>
    <div class="hours">
      <div>Business Hours:</div>
      <div class="row"><span class="days">Mon &amp; Wed</span><span>– <strong>9:30am to 6:00pm</strong></span></div>
      <div class="row"><span class="days">Tue, Thu &amp; Fri</span><span>– <strong>9:30am to 5:30pm</strong></span></div>
    </div>
  </section>

  <section class="office" style="top:882px">
    <div class="office-mark"></div>
    <div class="office-name">Hale &amp; Brook Eyecare</div>
    <ul class="contact">
      <li>
        <svg width="15" height="14" viewBox="0 0 15 14"><path d="M7.5 1 L14 7 H12 V13 H9 V9 H6 V13 H3 V7 H1 Z" fill="#3b8fd6"/></svg>
        <span>732 Linden Avenue<br>Between 22nd and 23rd Streets</span>
      </li>
      <li>
        <svg width="15" height="15" viewBox="0 0 15 15"><circle cx="7.5" cy="7.5" r="6.5" fill="none" stroke="#3b8fd6" stroke-width="1.3"/><path d="M5 4 L6.5 4 L7 6 L6 6.8 C6.5 8 7.2 8.7 8.2 9.2 L9 8.2 L11 8.7 L11 10.2 C8 10.6 4.6 7.2 5 4 Z" fill="#3b8fd6"/></svg>
        <span>(212) 555-0172</span>
      </li>
      <li>
        <svg width="15" height="15" viewBox="0 0 15 15" fill="none" stroke="#3b8fd6" stroke-width="1.2"><circle cx="7.5" cy="7.5" r="6.5"/><ellipse cx="7.5" cy="7.5" rx="3" ry="6.5"/><line x1="1" y1="7.5" x2="14" y2="7.5"/><line x1="2" y1="4.3" x2="13" y2="4.3"/><line x1="2" y1="10.7" x2="13" y2="10.7"/></svg>
        <span>www.halebrookeyes.com</span>
      </li>
    </ul>
    <div class="hours">
      <div>Business Hours:</div>
      <div class="row"><span class="days">Mon &amp; Thu</span><span>– <strong>9:00am to 7:30pm</strong></span></div>
      <div class="row"><span class="days">Tue, Wed &amp; Fri</span><span>– <strong>9:00am to 6pm</strong></span></div>
      <div class="row"><span class="days">Sat</span><span>– <strong>9:00am to 1:00pm</strong></span></div>
    </div>
  </section>
</main>
</body>
</html>
```